Modern card design needed for building development company

We are looking for a sharp modern new look for our business cards.
We are a New Zealand based company called TKV Ventures NZ LTD that specialises in subdividing large sections, housing and commercial buildings.
We have attached a photo of the current logo and would like to see it improved somehow as it looks a bit dated.
We are open to any colours.

Target Market(s)

Investors, Property buyers

Industry/Entity Type

Investment

Contact Information for Business Card

TKV VENTURES NZ LTD
www.tkvventuresnz.co.nz

Howard Pennick
Phone +64 21 843 192
Email hdpennick@fernmail.co.nz

Font styles to use
Serif
Sans Serif

Colors
0792cd
33a6d7
85cae6
6b449b
886aae
f04a50
ec1f27
f37122
f68d4d

Requirements
Must have
• Please try and make the logo more modern or if you have a similar one we would like to see it.

```html
<!DOCTYPE html>
<html lang="en">
<head>
<meta charset="utf-8">
<title>TKV Ventures NZ LTD – Business Card</title>
<link rel="stylesheet" href="https://fonts.googleapis.com/css2?family=Abel&family=Ubuntu:wght@400&display=swap">
<style>
  :root {
    --card-orange: #f08c4b;
    --ink: #2b2b2b;
    --brick: #9b2532;
    --gap: #ffffff;
  }
  html, body {
    margin: 0;
    padding: 0;
    width: 1200px;
    height: 349px;
    overflow: hidden;
    background: var(--gap);
  }
  .sheet {
    position: relative;
    width: 1200px;
    height: 349px;
  }
  .card {
    position: absolute;
    top: 0;
    height: 349px;
    background: var(--card-orange);
    overflow: hidden;
  }
  .card--front { left: 0; width: 596px; }
  .card--back { left: 604px; width: 596px; }

  .brand-mark {
    position: absolute;
    left: 0;
    width: 596px;
    top: 62px;
    display: flex;
    align-items: center;
    justify-content: center;
    gap: 10px;
  }
  .brand-mark__square {
    width: 44px;
    height: 44px;
    background: var(--brick);
  }
  .brand-mark__name {
    font-family: "Ubuntu", sans-serif;
    font-weight: 400;
    font-size: 17px;
    color: var(--brick);
    letter-spacing: 0.5px;
  }

  .company-name {
    position: absolute;
    left: 0;
    width: 596px;
    top: 138px;
    margin: 0;
    text-align: center;
    font-family: "Ubuntu", sans-serif;
    font-weight: 400;
    font-size: 30px;
    letter-spacing: 0.6px;
    color: var(--ink);
  }
  .company-url {
    position: absolute;
    left: 0;
    width: 596px;
    top: 175px;
    margin: 0;
    text-align: center;
    font-family: "Abel", sans-serif;
    font-size: 22px;
    color: var(--ink);
  }
  .contact {
    position: absolute;
    left: 0;
    width: 596px;
    top: 250px;
    margin: 0;
    text-align: center;
    font-family: "Abel", sans-serif;
    font-size: 19px;
    line-height: 24.5px;
    color: var(--ink);
    font-style: normal;
  }
  .contact span { display: block; }

  .back-mark {
    position: absolute;
    left: 0;
    width: 596px;
    top: 0;
    height: 349px;
    display: flex;
    flex-direction: column;
    align-items: center;
    justify-content: center;
    gap: 22px;
  }
  .back-mark__square {
    width: 110px;
    height: 110px;
    background: var(--brick);
  }
  .back-mark__name {
    font-family: "Ubuntu", sans-serif;
    font-weight: 400;
    font-size: 30px;
    letter-spacing: 1px;
    color: var(--brick);
  }
</style>
</head>
<body>
<main class="sheet">
  <section class="card card--front" aria-label="Card front">
    <div class="brand-mark">
      <span class="brand-mark__square" aria-hidden="true"></span>
      <span class="brand-mark__name">TKV Ventures NZ LTD</span>
    </div>
    <h1 class="company-name">TKV VENTURES NZ LTD</h1>
    <p class="company-url">www.tkvventuresnz.co.nz</p>
    <address class="contact">
      <span class="contact__name">Howard Pennick</span>
      <span class="contact__phone">Phone: +64 21 843 192</span>
      <span class="contact__email">Email: hdpennick@fernmail.co.nz</span>
    </address>
  </section>

  <section class="card card--back" aria-label="Card back">
    <div class="back-mark">
      <span class="back-mark__square" aria-hidden="true"></span>
      <span class="back-mark__name">TKV Ventures NZ LTD</span>
    </div>
  </section>
</main>
</body>
</html>
```